6 page (for now) squarespace website design for a Mobile Fitness small business

My sons California based small business "BrellaFit Coaching" with new subsidiary called "BrellaFit 4 Kids". I don't understand coding the website, is that the function squarespace provides?
In the end I want a working website, squarespace, I have a google workspace domain, email and subscription to squarespace & google workspace. URLs include brellafitcoaching.example and brellafit4kids.example. I have an idea of what I am looking for in a website and I have some examples of website designs I like, but I am 100% open to your design concepts and artistic flair. email is morgan@brellafitcoaching.example
I am looking for someone to design the site, help me understand how to make "minor" changes and hopefully have a long term relationship on the tech side of the business. I need an Idea of pricing for future changes (Rate T&M).
There are 2 businesses so I need a way to incorporate both the main company and a subsidiary into 1 website or link it somehow. I am open to your suggestions how to accomplish that. Do I need 2 completely separate websites or can it be done on 1 site directing you to different pages. I read conflicting info if it is a BAD idea to link 2 different websites so I will defer to your advice.
Below are the pages I need designed:
- Home Page- BrellaFit Coaching
- Home Page- BrellaFit 4 Kids (Homeschool market)
- Member Page (subscription service?)
- Workouts- with video clips 1-6 min each
- About
- Contact
- FAQ's
Future work & page designs:
- Store with training subscriptions & a few merch items
- Booking Appointments
- Bookshelf
- email campaign
-Blog
I like the feel of this website:
https://quillstride.example/

```html
<!DOCTYPE html>
<html lang="en">
<head>
<meta charset="utf-8">
<title>BrellaFit Coaching</title>
<link href="https://fonts.googleapis.com/css2?family=Montserrat:wght@300;400;600;700&family=Roboto:wght@400;500;700&display=swap" rel="stylesheet">
<style>
:root{
  --gold:#d2ad7f;
  --band:#d4b28a;
  --ink:#111;
  --text:#777;
  --white:#fff;
}
*{margin:0;padding:0;box-sizing:border-box}
html,body{width:1200px;height:4107px;overflow:hidden}
body{position:relative;background:var(--white);font-family:'Roboto',Arial,sans-serif;color:var(--ink)}
.abs{position:absolute}
.btn{position:absolute;display:flex;align-items:center;justify-content:center;gap:10px;font:700 12.5px 'Roboto',Arial,sans-serif;color:var(--white);text-transform:uppercase;background:var(--gold);border-radius:3px;letter-spacing:.2px}
.btn.dark{background:#000}
.btn .dot{width:12px;height:12px;border-radius:50%;background:var(--white);display:flex;align-items:center;justify-content:center}
.btn .dot svg{width:6px;height:6px}
.btn.dark .dot svg path{fill:#000}
.btn .dot svg path{fill:var(--gold)}

/* hero */
.hero{left:0;top:0;width:1200px;height:625px;background:linear-gradient(100deg,#8e8e8c 0%,#a9a8a4 35%,#7a756f 60%,#c8c6c2 100%)}
.brand{display:flex;align-items:center;gap:10px;font:400 19px 'Montserrat',Arial,sans-serif;letter-spacing:3px;text-transform:uppercase}
.brand .mark{width:14px;height:14px;border-radius:50%;background:currentColor}
.hero .brand{left:108px;top:42px;color:var(--white)}
.nav{display:flex;gap:22px;font:500 13.5px 'Roboto',Arial,sans-serif;color:var(--white)}
.hero .nav{left:412px;top:45px}
.nav .active{color:var(--gold)}
.hero-title{left:108px;top:258px;font:300 45px 'Montserrat',Arial,sans-serif;color:var(--white);letter-spacing:.5px}
.hero-title b{font-weight:700}
.hero-copy{left:112px;top:334px;width:470px;font:500 16px/25px 'Roboto',Arial,sans-serif;color:var(--white)}

/* section headings */
.heading{font:300 26px 'Montserrat',Arial,sans-serif;text-transform:uppercase;letter-spacing:.5px}
.heading b{font-weight:700}
.heading.center{left:0;width:1200px;text-align:center}
.orn{width:14px;height:14px;border-radius:50%;border:2px solid currentColor}

/* service rows */
.photo{background:var(--white);padding:6px;box-shadow:0 0 6px rgba(0,0,0,.18)}
.photo div{width:100%;height:100%}
.svc-title{font:600 28px 'Montserrat',Arial,sans-serif}
.copy{width:450px;font:400 14.5px/25.6px 'Roboto',Arial,sans-serif;color:var(--text);text-align:justify}

/* workouts */
.workouts{left:0;top:2490px;width:1200px;height:488px;background:linear-gradient(180deg,#6f7a86 0%,#8a8f8c 35%,#6d6a3d 65%,#3f4a2a 100%)}
.play{left:570px;top:2835px;width:60px;height:60px;border-radius:50%;border:3px solid rgba(255,255,255,.85);display:flex;align-items:center;justify-content:center}
.play span{width:38px;height:38px;border-radius:50%;background:rgba(255,255,255,.9);display:flex;align-items:center;justify-content:center}

/* newsletter */
.newsletter{left:0;top:3556px;width:1200px;height:308px;background:var(--band)}
.field{position:absolute;top:3690px;width:318px;height:47px;background:var(--white);display:flex;align-items:center;justify-content:space-between;padding:0 18px;font:400 12.5px 'Roboto',Arial,sans-serif;color:#999}

/* footer */
.footer .brand{left:108px;top:3975px;color:#111}
.social{position:absolute;top:4001px;width:32px;height:32px;border-radius:50%;border:1px solid #e2c8a6}
</style>
</head>
<body>

<!-- HERO -->
<section class="abs hero" role="img" aria-label="Muscular man and woman lifting dumbbells in a misty gym"></section>
<div class="abs brand"><span class="mark"></span>BrellaFit</div>
<nav class="abs nav" style="left:412px;top:46px">
  <span class="active">Home</span><span>Member</span><span>Workouts</span><span>About</span><span>FAQ</span><span>Blog</span><span>Contact</span>
</nav>
<a class="btn" style="left:873px;top:33px;width:215px;height:43px">Book an appointment<span class="dot"><svg viewBox="0 0 6 6"><path d="M1 0l4 3-4 3z"/></svg></span></a>
<h1 class="abs hero-title">BRELLAFIT <b>COACHING</b></h1>
<p class="abs hero-copy">Lorem ipsum dolor sit amet, consectetur adipiscing elit, sed do eiusmod tempor incididunt ut labore</p>
<a class="btn" style="left:112px;top:412px;width:188px;height:44px">BrellaFit Coaching<span class="dot"><svg viewBox="0 0 6 6"><path d="M1 0l4 3-4 3z"/></svg></span></a>
<a class="btn dark" style="left:327px;top:412px;width:188px;height:44px">BrellaFit 4 Kids<span class="dot"><svg viewBox="0 0 6 6"><path d="M1 0l4 3-4 3z"/></svg></span></a>

<!-- SUBSCRIPTION SERVICE -->
<span class="abs orn" style="left:593px;top:691px;color:#111"></span>
<h2 class="abs heading center" style="top:708px">Subscription <b>Service</b></h2>

<figure class="abs photo" style="left:110px;top:789px;width:440px;height:363px"><div role="img" aria-label="Woman in sportswear drinking from a shaker bottle" style="background:linear-gradient(120deg,#d9cbb8,#eee7dc 55%,#c8b8a3)"></div></figure>
<h3 class="abs svc-title" style="left:634px;top:832px">Personal Training</h3>
<p class="abs copy" style="left:637px;top:883px">Sed ut perspiciatis unde omnis iste natus error sit voluptatem accusantium doloremque laudantium, totam rem aperiam, eaque ipsa quae ab illo inventore veritatis et quasi architecto beatae vitae dicta sunt explicabo. Nemo enim ipsam voluptatem quia voluptas sit aspernatur aut odit aut fugit, sed quia consequuntur magni dolores eos qui ratione voluptatem sequi nesciunt.</p>
<a class="btn" style="left:638px;top:1062px;width:146px;height:43px">Learn more<span class="dot"><svg viewBox="0 0 6 6"><path d="M1 0l4 3-4 3z"/></svg></span></a>

<h3 class="abs svc-title" style="left:110px;top:1243px">Online Training</h3>
<p class="abs copy" style="left:112px;top:1294px">Sed ut perspiciatis unde omnis iste natus error sit voluptatem accusantium doloremque laudantium, totam rem aperiam, eaque ipsa quae ab illo inventore veritatis et quasi architecto beatae vitae dicta sunt explicabo. Nemo enim ipsam voluptatem quia voluptas sit aspernatur aut odit aut fugit, sed quia consequuntur magni dolores eos qui ratione voluptatem sequi nesciunt.</p>
<a class="btn" style="left:113px;top:1473px;width:146px;height:43px">Learn more<span class="dot"><svg viewBox="0 0 6 6"><path d="M1 0l4 3-4 3z"/></svg></span></a>
<figure class="abs photo" style="left:649px;top:1200px;width:440px;height:364px"><div role="img" aria-label="Smiling woman with glasses taking notes at a laptop" style="background:linear-gradient(120deg,#c9c2b6,#e6e3dc 55%,#b7c1c8)"></div></figure>

<figure class="abs photo" style="left:110px;top:1612px;width:440px;height:365px"><div role="img" aria-label="Nutritionist with clipboard talking with an older woman at a meal table" style="background:linear-gradient(120deg,#d8d2c6,#efece6 50%,#c9b99e)"></div></figure>
<h3 class="abs svc-title" style="left:634px;top:1655px">Nutritional Guidance</h3>
<p class="abs copy" style="left:637px;top:1706px">Sed ut perspiciatis unde omnis iste natus error sit voluptatem accusantium doloremque laudantium, totam rem aperiam, eaque ipsa quae ab illo inventore veritatis et quasi architecto beatae vitae dicta sunt explicabo. Nemo enim ipsam voluptatem quia voluptas sit aspernatur aut odit aut fugit, sed quia consequuntur magni dolores eos qui ratione voluptatem sequi nesciunt.</p>
<a class="btn" style="left:638px;top:1885px;width:146px;height:43px">Learn more<span class="dot"><svg viewBox="0 0 6 6"><path d="M1 0l4 3-4 3z"/></svg></span></a>

<h3 class="abs svc-title" style="left:110px;top:2066px">Business Coaching</h3>
<p class="abs copy" style="left:112px;top:2117px">Sed ut perspiciatis unde omnis iste natus error sit voluptatem accusantium doloremque laudantium, totam rem aperiam, eaque ipsa quae ab illo inventore veritatis et quasi architecto beatae vitae dicta sunt explicabo. Nemo enim ipsam voluptatem quia voluptas sit aspernatur aut odit aut fugit, sed quia consequuntur magni dolores eos qui ratione voluptatem sequi nesciunt.</p>
<a class="btn" style="left:113px;top:2296px;width:146px;height:43px">Learn more<span class="dot"><svg viewBox="0 0 6 6"><path d="M1 0l4 3-4 3z"/></svg></span></a>
<figure class="abs photo" style="left:649px;top:2024px;width:440px;height:364px"><div role="img" aria-label="Woman in yellow top mixing a drink in a bright kitchen" style="background:linear-gradient(120deg,#aebcc5,#d6dde0 50%,#c4a98a)"></div></figure>

<!-- OUR WORKOUTS -->
<section class="abs workouts" role="img" aria-label="Woman with outstretched arms in a field of yellow flowers"></section>
<span class="abs orn" style="left:593px;top:2577px;color:#fff"></span>
<h2 class="abs heading center" style="top:2594px;color:#fff">Our <b style="color:var(--gold)">Workouts</b></h2>
<p class="abs" style="left:110px;top:2660px;width:980px;text-align:center;font:400 14.5px/24px 'Roboto',Arial,sans-serif;color:#fff">Lorem ipsum dolor sit amet, consectetur adipiscing elit, sed do eiusmod tempor incididunt ut labore et dolore magna aliqua. Ut enim ad minim veniam, quis nostrud exercitation ullamco laboris nisi ut aliquip ex ea commodo consequat. Duis aute irure dolor in reprehenderit in voluptate velit esse cillum dolore eu fugiat nulla pariatur. Excepteur sint occaecat cupidatat non proident, sunt in culpa qui officia deserunt mollit anim id est laborum</p>
<a class="btn" style="left:507px;top:2758px;width:186px;height:43px">View all videos<span class="dot"><svg viewBox="0 0 6 6"><path d="M1 0l4 3-4 3z"/></svg></span></a>
<div class="abs play"><span><svg width="12" height="14" viewBox="0 0 12 14"><path d="M1 0l11 7-11 7z" fill="#c9a57a"/></svg></span></div>

<!-- ABOUT -->
<figure class="abs photo" style="left:110px;top:3092px;width:440px;height:364px"><div role="img" aria-label="Woman in pink top pouring a protein shake in a kitchen" style="background:linear-gradient(120deg,#d7d4cf,#f0eeea 50%,#d9b4a6)"></div></figure>
<span class="abs orn" style="left:644px;top:3130px;color:#111"></span>
<h2 class="abs heading" style="left:637px;top:3148px">About <b>Us</b></h2>
<p class="abs copy" style="left:637px;top:3200px">Sed ut perspiciatis unde omnis iste natus error sit voluptatem accusantium doloremque laudantium, totam rem aperiam, eaque ipsa quae ab illo inventore veritatis et quasi architecto beatae vitae dicta sunt explicabo. Nemo enim ipsam voluptatem quia voluptas sit aspernatur aut odit aut fugit, sed quia consequuntur magni dolores eos qui ratione voluptatem sequi nesciunt.</p>
<a class="btn" style="left:638px;top:3381px;width:146px;height:43px">Learn more<span class="dot"><svg viewBox="0 0 6 6"><path d="M1 0l4 3-4 3z"/></svg></span></a>

<!-- NEWSLETTER -->
<section class="abs newsletter"></section>
<span class="abs orn" style="left:593px;top:3613px;color:#fff"></span>
<h2 class="abs heading center" style="top:3631px;color:#fff">Newsletter <b>Subscription</b></h2>
<div class="field" style="left:110px">First Name<svg width="10" height="11" viewBox="0 0 10 11"><circle cx="5" cy="3" r="2.6" fill="#333"/><path d="M0 11c0-4 2-5.5 5-5.5s5 1.5 5 5.5z" fill="#333"/></svg></div>
<div class="field" style="left:440px">Last Name<svg width="10" height="11" viewBox="0 0 10 11"><circle cx="5" cy="3" r="2.6" fill="#333"/><path d="M0 11c0-4 2-5.5 5-5.5s5 1.5 5 5.5z" fill="#333"/></svg></div>
<div class="field" style="left:771px">Email Address<svg width="12" height="9" viewBox="0 0 12 9"><rect width="12" height="9" fill="#333"/><path d="M0 0l6 5 6-5" stroke="#fff" fill="none"/></svg></div>
<a class="btn dark" style="left:507px;top:3755px;width:186px;height:47px;border-radius:2px">Subscribe now</a>

<!-- FOOTER -->
<footer class="footer">
  <div class="abs brand"><span class="mark"></span>BrellaFit</div>
  <p class="abs" style="left:110px;top:4031px;font:400 12.5px 'Roboto',Arial,sans-serif;color:#222">© 2022 BrellaFit. All Rights Reserved</p>
  <nav class="abs nav" style="left:647px;top:3960px;gap:20px;color:#111;font-size:13px"><span>Home</span><span>Member</span><span>Workouts</span><span>About</span><span>FAQ</span><span>Blog</span><span>Contact</span></nav>
  <span class="social" style="left:905px"></span>
  <span class="social" style="left:951px"></span>
  <span class="social" style="left:996px"></span>
  <span class="social" style="left:1042px"></span>
</footer>

</body>
</html>
```